New web design for a service provider in the medical field

We are looking for a new design for our website. We are a company that repairs and sells medical endoscopes. Our customers include doctors and hospitals. Our current website can be found at https://lumenfix.example/en/lumenfix-english.
We need a new web design (without programming) for the following 3 pages:
-Startpage https://lumenfix.example/en/lumenfix-english/
-Used endoscopes https://lumenfix.example/en/used-endoscopes/
-Purchase https://lumenfix.example/en/purchase/
The design should be modern and stylish.
The blue color of the logo should be reflected on the page, but not too intrusive.
I have uploaded the images from the header. If more images are needed, let me know and I will upload them.

Target Market(s)
Doctors and hospitals

```html
<!DOCTYPE html>
<html lang="en">
<head>
<meta charset="utf-8">
<title>LumenFix – Endoscope Repair and Sale</title>
<link rel="stylesheet" href="https://fonts.googleapis.com/css2?family=Inter:wght@400;500;600&family=Lora:wght@400;500&display=swap">
<style>
:root{
  --blue:#0b72bd;
  --blue-mid:#79aedc;
  --blue-soft:#c9dff2;
  --bg-tint:#e4edf6;
  --ink:#1b1f24;
  --muted:#5a6068;
  --line:#d3d8de;
  --white:#fff;
  --serif:'Lora', Georgia, serif;
  --sans:'Inter', Arial, sans-serif;
}
*{box-sizing:border-box;margin:0;padding:0}
html,body{width:1200px;height:3661px;overflow:hidden}
body{position:relative;font-family:var(--sans);color:var(--ink);background:var(--white)}
.abs{position:absolute}
a{color:inherit;text-decoration:none}

/* top bar */
.topbar{left:0;top:0;width:1200px;height:48px;background:var(--blue);color:var(--white);font-size:12.5px}
.topbar .links{position:absolute;left:85px;top:16px;display:flex;gap:22px}
.topbar .contact{position:absolute;right:24px;top:15px;display:flex;gap:30px;align-items:center}
.topbar .contact span{display:flex;align-items:center;gap:8px}

/* nav */
.nav{left:0;top:48px;width:1200px;height:104px;background:var(--white)}
.logo-box{left:85px;top:48px;width:224px;height:147px;background:var(--white);z-index:3;display:flex;align-items:center;justify-content:center;gap:10px}
.brand{font-family:var(--sans);font-weight:600;font-size:25px;color:var(--blue)}
.brand-dot{width:14px;height:14px;border-radius:50%;background:var(--blue)}
.menu{position:absolute;left:339px;top:42px;display:flex;gap:21px;font-size:14px;color:var(--ink)}
.menu .active{color:var(--blue)}
.menu .drop::after{content:"⌄";font-size:11px;margin-left:3px}

/* hero */
.hero-panel{left:0;top:152px;width:600px;height:519px;background:var(--blue);color:var(--white)}
.hero-panel .kicker{position:absolute;left:87px;top:116px;font-weight:600;font-size:19px}
.hero-panel h1{position:absolute;left:87px;top:154px;padding-left:21px;border-left:3px solid var(--white);font-family:var(--serif);font-weight:400;font-size:45px;line-height:54px;width:480px}
.hero-panel p{position:absolute;left:87px;top:278px;width:470px;font-size:15.5px;line-height:23px}
.btn{display:inline-flex;align-items:center;justify-content:center;background:var(--white);color:var(--blue);border-radius:24px;font-size:14px;font-weight:500}
.hero-panel .btn{position:absolute;left:87px;top:395px;width:128px;height:47px}
.hero-photo{left:600px;top:152px;width:600px;height:519px;background:linear-gradient(120deg,#e3e4e5 0%,#c5c7c9 45%,#6e7174 80%,#a8abad 100%)}

/* intro */
.faulty{left:0;top:712px;width:1200px;text-align:center}
.faulty h2{font-family:var(--serif);font-weight:400;font-size:33px;line-height:41px;width:620px;margin:0 auto}
.faulty p{margin-top:26px;font-size:15px;color:var(--muted)}
.faulty p a{color:var(--ink);font-weight:500;border-bottom:1.5px solid var(--ink)}

.tint{left:0;top:883px;width:1200px;height:360px;background:linear-gradient(180deg,var(--bg-tint) 0%,#eef3f9 70%,var(--white) 100%)}
.about-title{left:85px;top:971px;width:420px;font-family:var(--serif);font-weight:400;font-size:30px;line-height:35px}
.about-text{left:599px;top:972px;width:510px;font-size:15.5px;line-height:23px;color:#3b4148}
.about-text p+p{margin-top:23px}

/* service cards */
.card{top:1250px;width:325px;height:367px;border-radius:6px;padding:36px 30px 0;overflow:hidden}
.card .tag{font-size:14.5px;font-weight:600;letter-spacing:.2px}
.card h3{font-family:var(--serif);font-weight:400;font-size:26px;line-height:33px;margin-top:6px;height:70px}
.card p{font-size:11.5px;line-height:19.5px;margin-top:16px;width:268px}
.card .more{font-size:13.5px;margin-top:16px;font-weight:500}
.card .shot{position:absolute;right:0;bottom:0;border-radius:40% 0 0 0}
.c1{left:85px;background:var(--blue);color:var(--white)}
.c2{left:436px;background:var(--blue-mid);color:var(--white)}
.c3{left:789px;background:var(--blue-soft);color:var(--ink)}
.c3 .tag,.c3 .more{color:var(--blue)}

/* why */
.why-deco{left:967px;top:1635px;width:233px;height:256px;background:radial-gradient(circle at 50% 50%,#b9c9dc 0%,#e7eef6 55%,var(--white) 75%)}
.label{font-size:19px;font-weight:600;color:var(--blue)}
.why-label{left:85px;top:1705px}
.why-title{left:85px;top:1747px;width:560px;font-family:var(--serif);font-weight:400;font-size:33px;line-height:46px}
.why-rule{left:85px;top:1863px;width:880px;height:1px;background:var(--line)}
.feat{width:330px;display:flex;gap:20px}
.feat .ico{flex:none;width:54px;height:54px;border-radius:50%;background:var(--blue);display:flex;align-items:center;justify-content:center}
.feat h4{font-family:var(--serif);font-weight:400;font-size:21px;line-height:28px}
.feat p{font-size:13.5px;line-height:19.5px;color:var(--muted);margin-top:10px}

/* help */
.help{left:85px;top:2325px;width:1028px;height:428px;background:var(--blue);border-radius:28px;overflow:hidden;color:var(--white)}
.help .shot{position:absolute;left:0;top:0;width:480px;height:428px;background:linear-gradient(110deg,#8a8f94 0%,#d6c5b2 45%,#3a4048 75%,var(--blue) 100%)}
.help h2{position:absolute;left:530px;top:76px;font-family:var(--serif);font-weight:400;font-size:33px}
.help p{position:absolute;left:531px;top:137px;width:380px;font-size:15.5px;line-height:23px}
.help .btn{position:absolute;left:531px;top:297px;width:181px;height:48px}

/* outcome */
.outcome-band{left:0;top:2790px;width:1200px;height:500px;background:linear-gradient(180deg,var(--white) 0%,var(--white) 55%,#e6eef6 100%)}
.out-label{left:0;top:2845px;width:1200px;text-align:center}
.out-title{left:0;top:2880px;width:1200px;text-align:center;font-family:var(--serif);font-weight:400;font-size:33px}
.dash{left:158px;top:3017px;width:908px;border-top:1.5px dashed #b9c4cf}
.step{top:2957px;width:280px;text-align:center}
.step .num{width:60px;height:60px;border-radius:50%;background:var(--blue);color:var(--white);font-family:var(--serif);font-weight:500;font-size:23px;display:flex;align-items:center;justify-content:center;margin:0 auto}
.step h4{font-weight:500;font-size:19px;line-height:26px;margin-top:20px}
.step p{font-size:12px;line-height:19px;color:var(--muted);margin-top:10px}
.pager{left:545px;top:3188px;display:flex;gap:12px}
.pager i{display:block;height:7px;border-radius:4px;background:#86b7e0;width:20px}
.pager i:first-child{width:48px;background:var(--blue)}

/* footer */
.foot-links{top:3428px;display:flex;gap:32px;font-size:14px}
.foot-brand{left:500px;top:3410px;width:200px;display:flex;justify-content:center;align-items:center;gap:10px}
.foot-rule{left:85px;top:3515px;width:1028px;height:1px;background:var(--line)}
.copy{left:0;top:3535px;width:1200px;text-align:center;font-size:14px}
.social{left:546px;top:3573px;display:flex;gap:16px}
.social span{width:43px;height:43px;border:1.5px solid var(--ink);border-radius:10px}
</style>
</head>
<body>

<div class="abs topbar">
  <div class="links"><a>Pick-up Order</a><a>About Us</a><a>Contact Us</a></div>
  <div class="contact">
    <span><svg width="16" height="12" viewBox="0 0 16 12" fill="none" stroke="#fff" stroke-width="1.2"><rect x=".6" y=".6" width="14.8" height="10.8" rx="1"/><path d="M1 1l7 6 7-6"/></svg>Email: info@lumenfix.example</span>
    <span><svg width="14" height="14" viewBox="0 0 14 14" fill="none" stroke="#fff" stroke-width="1.2"><path d="M3 1l2 3-1.5 1.5a8 8 0 0 0 5 5L10 9l3 2-1 2C6 13 1 8 1 2z"/></svg>Phone: +49 4000 555 120-0</span>
    <span>EN ⌄</span>
  </div>
</div>

<div class="abs nav">
  <nav class="menu">
    <a class="active">Home</a><a>Endoscope Repair</a><a class="drop">Used Endoscopes</a><a>Endoscopy Systems</a><a class="drop">Endoscopy Accessories</a><a>Purchase</a>
  </nav>
</div>
<div class="abs logo-box"><span class="brand-dot"></span><span class="brand">LumenFix</span></div>

<section class="abs hero-panel">
  <div class="kicker">Your Future - Our Service</div>
  <h1>Put Your Endoscope in Reliable Hands!</h1>
  <p>LumenFix GmbH is specialised in the repair and sale of Orivon, Pentrel and Fujara flexible medical endoscopes. As a service-oriented company, we are at your side with our knowledge and skills!</p>
  <a class="btn">Contact Us</a>
</section>
<div class="abs hero-photo" role="img" aria-label="Close-up photo of an endoscope control handle with angulation knobs"></div>

<section class="abs faulty">
  <h2>Faulty Endoscope?We ensure quick and smooth repairs!</h2>
  <p>Simple place a <a>Pick Up Order</a></p>
</section>

<div class="abs tint"></div>
<h2 class="abs about-title">Endoscope repairs and second hand endoscopes from LumenFix – cause the outcome matters!</h2>
<div class="abs about-text">
  <p>LumenFix is a privileged partner for the start-up facility or optimisation of existing healthcare facilities, doctor’s offices and hospitals. The quality and reliability of our products and our offered service are our best advertisement!</p>
  <p>As a result of optimised processes and highly qualified specialists in our company, we can work very quickly and with high quality for your benefit of least possible restrictions in your doctor’s office or in your hospital.</p>
</div>

<article class="abs card c1">
  <div class="tag">REPAIR</div>
  <h3>Endoscope Repair Service</h3>
  <p>Manufacturer-independent we repair and maintain endoscopes, individual components (e.g. processors or light sources), accessories and peripherals of the manufacturers Orivon, Pentrel and Fujara.</p>
  <div class="more">Repair Request »</div>
  <div class="shot" role="img" aria-label="Photo of a coiled flexible endoscope" style="width:170px;height:100px;background:linear-gradient(135deg,#0b72bd,#2a3440)"></div>
</article>
<article class="abs card c2">
  <div class="tag">SALE</div>
  <h3>Used Endoscopes</h3>
  <p>Our regular stock includes refurbished gastroscopes, coloscopes, bronchoscopes, cystoscopes and duodenoscopes from the well-known manufacturers Orivon, Pentrel and Fujara.</p>
  <div class="more">Purchase Request »</div>
  <div class="shot" role="img" aria-label="Photo of an endoscope with a coiled cable" style="width:190px;height:150px;background:linear-gradient(135deg,#79aedc,#22282e)"></div>
</article>
<article class="abs card c3">
  <div class="tag">PURCHASE</div>
  <h3>Used Endoscopes</h3>
  <p>We are very interested in buying your old endoscopes – even defective and dismantled! We offer fair conditions! Please contact us for a purchase offer!</p>
  <div class="more">Sell Device »</div>
  <div class="shot" role="img" aria-label="Photo of a black endoscope connector device" style="width:190px;height:120px;background:linear-gradient(135deg,#c9dff2,#1c2026)"></div>
</article>

<div class="abs why-deco" role="img" aria-label="Decorative photo of a looped flexible endoscope"></div>
<div class="abs label why-label">Why Choose Us</div>
<h2 class="abs why-title">LumenFix GmbH, your decision for your future</h2>
<div class="abs why-rule"></div>

<div class="abs feat" style="left:85px;top:1901px">
  <span class="ico"><svg width="28" height="28" viewBox="0 0 28 28" fill="none" stroke="#fff" stroke-width="1.6"><circle cx="16" cy="14" r="8"/><path d="M16 9v5l3 2M2 10h6M1 14h6M2 18h6"/></svg></span>
  <div><h4>Fast Repairs</h4><p>Keep potential disruptions in your doctor’s office or in your hospital at minimum as a result of optimized processes and highly qualified specialists in our company</p></div>
</div>
<div class="abs feat" style="left:436px;top:1901px">
  <span class="ico"><svg width="26" height="26" viewBox="0 0 26 26" fill="none" stroke="#fff" stroke-width="1.6"><path d="M3 12L13 3l10 9M6 10v12h14V10M11 22v-6h4v6"/></svg></span>
  <div><h4>On-site Service</h4><p>We will gladly pay you a visit to to carry out analysis and repairs on site. Due to our many years of experience – it doesn’t get any faster (whigleithin a 250 km range)</p></div>
</div>
<div class="abs feat" style="left:788px;top:1901px">
  <span class="ico"><svg width="26" height="26" viewBox="0 0 26 26" fill="none" stroke="#fff" stroke-width="1.6"><circle cx="13" cy="13" r="10"/><path d="M8 13l4 4 8-9"/></svg></span>
  <div><h4>Without a Maintenance Contract</h4><p>No subscription or other maintenance contract, but one-time and sustainable repair work</p></div>
</div>
<div class="abs feat" style="left:85px;top:2077px">
  <span class="ico"><svg width="26" height="26" viewBox="0 0 26 26" fill="none" stroke="#fff" stroke-width="1.6"><circle cx="13" cy="10" r="7"/><path d="M9 16l-2 8 6-3 6 3-2-8"/></svg></span>
  <div><h4>Highly Cost Efficient</h4><p>Benefit from our first class recommendations and implementation by our experienced staff. Our goals is to find the best solutions together with you at the best lowest price point.</p></div>
</div>
<div class="abs feat" style="left:436px;top:2077px">
  <span class="ico"><svg width="26" height="26" viewBox="0 0 26 26" fill="none" stroke="#fff" stroke-width="1.6"><path d="M3 12h5v11H3zM8 13l4-9c2 0 3 1 3 3l-1 4h7c1 0 2 1 2 2l-2 8c0 1-1 2-2 2H8"/></svg></span>
  <div><h4>Loan Equipment Service</h4><p>Use our service of high-quality loan devices during the downtime of your defective endoscope (limited to stock)</p></div>
</div>
<div class="abs feat" style="left:788px;top:2077px">
  <span class="ico"><svg width="26" height="26" viewBox="0 0 26 26" fill="none" stroke="#fff" stroke-width="1.6"><circle cx="13" cy="10" r="7"/><circle cx="13" cy="10" r="3.5"/><path d="M8 15l-3 8 4-1 2 3 2-5 2 5 2-3 4 1-3-8"/></svg></span>
  <div><h4>First class service</h4><p>Our clients always come first!</p></div>
</div>

<section class="abs help">
  <div class="shot" role="img" aria-label="Photo of a gloved hand holding an endoscope control section"></div>
  <h2>How can we help you?</h2>
  <p>LumenFix GmbH is specialized in repairing and saling flexible endoscopes along with accessories and consumables. We offer endoscopes, processors, light sources, accessories and much more – with a focus on the manufacturers Orivon, Pentrel and Fujara.</p>
  <a class="btn">Send Us A Message</a>
</section>

<div class="abs outcome-band"></div>
<div class="abs label out-label">Our Outcome</div>
<h2 class="abs out-title">Cause The Outcome Matters!</h2>
<div class="abs dash"></div>
<div class="abs step" style="left:18px"><div class="num">01</div><h4>One company for everyone</h4><p>We are a service provider for<br>doctors and hospitals!</p></div>
<div class="abs step" style="left:318px"><div class="num">02</div><h4>Experience characterises us</h4><p>Our team has many years of experience<br>in the business field!</p></div>
<div class="abs step" style="left:623px"><div class="num">03</div><h4>The product is close to<br>our hearts</h4><p>We repair and sell second hand,<br>flexible endoscopes!</p></div>
<div class="abs step" style="left:926px"><div class="num">04</div><h4>Guaranteed service</h4><p>You receive a six-month warranty<br>on all repairs!</p></div>
<div class="abs pager"><i></i><i></i><i></i></div>

<footer>
  <div class="abs foot-links" style="left:86px"><a>Informations</a><a>About Us</a><a>Contact Us</a></div>
  <div class="abs foot-brand"><span class="brand-dot"></span><span class="brand">LumenFix</span></div>
  <div class="abs foot-links" style="left:854px;gap:27px"><a>TOS</a><a>Copyrights</a><a>Privacy Policy</a></div>
  <div class="abs foot-rule"></div>
  <div class="abs copy">© 2022 LumenFix GmbH</div>
  <div class="abs social"><span aria-label="Social profile"></span><span aria-label="Social profile"></span></div>
</footer>

</body>
</html>
```